75th Anniversary Hang Tag

Hang tag that measures 4x4 and has a grommet hole to attached to all upholstery items that get shipped to our retailers. The hang tag is 2-sided and 4-color. I have attached a PowerPoint file to illustrate a concept. I look to you for better "creative" and "artistic" suggestions.

Target Market(s)

Furniture retailers and their consumers.

Industry/Entity Type

Home Furniture

Font styles to use
Sans Serif
Other font styles liked:
• Century Gothic

Colors
fbe7d2
f3f1f8
eaf1f7

Requirements
Must have
• Use all logos submitted. Would like a clean, upscale design. I prefer Century Gothic font.

```html
<!DOCTYPE html>
<html lang="en">
<head>
<meta charset="utf-8">
<title>Hollisfield 75th Anniversary Hang Tag</title>
<link rel="stylesheet" href="https://fonts.googleapis.com/css2?family=Jost:wght@400;700&family=Questrial&display=swap">
<style>
  :root {
    --bg-top: #e4e4e4;
    --bg-bottom: #f6f6f6;
    --tag-edge: #fbe7d2;
    --tag-light: #f9e3cb;
    --tag-deep: #efd2b2;
    --ruby: #8e1c22;
    --ruby-dark: #6d1418;
    --taupe: #a89684;
    --ink: #2b2b2b;
    --label: #666;
  }
  html, body { margin: 0; padding: 0; overflow: hidden; }
  body { width: 1200px; height: 1200px; background: linear-gradient(var(--bg-top), var(--bg-bottom)); }
  .sheet { display: block; width: 1200px; height: 1200px; }
  .side-label { font-family: "Questrial", sans-serif; font-weight: 700; font-size: 22px; fill: var(--label); letter-spacing: 0.5px; }
  .brand-name { font-family: "Jost", sans-serif; font-weight: 700; font-size: 32px; fill: var(--ruby); letter-spacing: 1px; }
  .tagline { font-family: "Questrial", sans-serif; font-size: 14px; fill: var(--ink); letter-spacing: 0.4px; }
  .pill-text { font-family: "Jost", sans-serif; font-size: 11px; fill: #fff; letter-spacing: 0.6px; }
  .company-name { font-family: "Jost", sans-serif; font-weight: 700; font-size: 21px; fill: var(--ruby); letter-spacing: 0.5px; }
  .contact { font-family: "Jost", sans-serif; font-size: 17px; fill: var(--ruby-dark); }
  .phone { font-family: "Jost", sans-serif; font-size: 26px; fill: var(--ruby-dark); }
  .web { font-family: "Jost", sans-serif; font-size: 17px; fill: var(--ruby-dark); }
  .motto { font-family: "Jost", sans-serif; font-size: 14.5px; fill: #fff; }
  .motto tspan.strong { font-weight: 700; }
  .social { font-family: "Jost", sans-serif; font-size: 18px; fill: var(--ruby-dark); }
</style>
</head>
<body>
<svg class="sheet" viewBox="0 0 1200 1200" xmlns="http://www.w3.org/2000/svg">
  <defs>
    <linearGradient id="tag-fill" x1="0" y1="0" x2="0" y2="1">
      <stop offset="0" stop-color="var(--tag-light)"/>
      <stop offset="1" stop-color="var(--tag-deep)"/>
    </linearGradient>
    <linearGradient id="badge-fill" x1="0" y1="0" x2="0" y2="1">
      <stop offset="0" stop-color="#b0454a"/>
      <stop offset="1" stop-color="#b9a896"/>
    </linearGradient>
    <filter id="tag-shadow" x="-10%" y="-10%" width="120%" height="120%">
      <feDropShadow dx="0" dy="2" stdDeviation="3" flood-color="#000" flood-opacity="0.45"/>
    </filter>
  </defs>

  <!-- Front tag -->
  <g class="tag tag-front">
    <polygon points="504,44 708,44 866,232 702,570 500,570 334,232" fill="var(--tag-edge)" filter="url(#tag-shadow)"/>
    <polygon class="tag-face" role="img" aria-label="Soft cream background with faint gemstone pattern"
             points="510,54 702,54 854,232 695,558 507,558 346,232" fill="url(#tag-fill)"/>
    <circle class="grommet" cx="600" cy="72" r="8" fill="#333"/>

    <rect class="anniversary-badge" role="img" aria-label="75th anniversary emblem with gemstone and ribbon banner"
          x="410" y="160" width="380" height="134" rx="10" fill="url(#badge-fill)"/>

    <text class="brand-name" x="600" y="324" text-anchor="middle">HOLLISFIELD</text>
    <text class="tagline" x="600" y="344" text-anchor="middle">HANDCRAFTED LIFESTYLE UPHOLSTERY</text>
    <line x1="480" y1="358" x2="720" y2="358" stroke="var(--ruby)" stroke-width="1.5"/>
    <rect x="506" y="351" width="188" height="15" rx="7" fill="var(--ruby)"/>
    <text class="pill-text" x="600" y="363" text-anchor="middle">AMERICAN MADE SINCE 1944</text>
  </g>
  <text class="side-label" x="598" y="604" text-anchor="middle">FRONT</text>

  <!-- Back tag -->
  <g class="tag tag-back">
    <polygon points="504,614 708,614 866,800 702,1140 500,1140 334,800" fill="var(--tag-edge)" filter="url(#tag-shadow)"/>
    <polygon class="tag-face" role="img" aria-label="Soft cream background with faint gemstone pattern"
             points="510,624 702,624 854,800 695,1128 507,1128 346,800" fill="url(#tag-fill)"/>
    <circle class="grommet" cx="600" cy="642" r="8" fill="#333"/>

    <circle class="brand-mark" cx="600" cy="714" r="42" fill="var(--ruby)"/>

    <line x1="390" y1="776" x2="810" y2="776" stroke="var(--ruby)" stroke-width="1.2"/>
    <text class="company-name" x="600" y="803" text-anchor="middle">HOLLISFIELD FURNITURE COMPANY</text>
    <line x1="390" y1="813" x2="810" y2="813" stroke="var(--ruby)" stroke-width="1.2"/>

    <g class="icon-pin" fill="none" stroke="var(--ruby-dark)" stroke-width="1.5">
      <circle cx="597" cy="828" r="10"/>
      <path d="M597,834 C593,829 592,826 592,824 A5,5 0 0 1 602,824 C602,826 601,829 597,834 Z" fill="var(--ruby-dark)" stroke="none"/>
      <circle cx="597" cy="824" r="1.8" fill="#f6dcc0" stroke="none"/>
    </g>
    <text class="contact" x="598" y="858" text-anchor="middle">482 N ELM AVENUE</text>
    <text class="contact" x="598" y="878" text-anchor="middle">HOLLISFIELD, WI 5482</text>

    <g class="icon-phone" fill="none" stroke="var(--ruby-dark)" stroke-width="1.5">
      <circle cx="518" cy="899" r="10"/>
      <path d="M513,894 L516,893 L518,897 L516,899 Q518,902 521,903 L523,901 L527,903 L526,906 Q518,907 513,894 Z" fill="var(--ruby-dark)" stroke="none"/>
    </g>
    <text class="phone" x="537" y="908">800-xxx-xxxx</text>

    <g class="icon-web" fill="none" stroke="var(--ruby-dark)" stroke-width="1.2">
      <circle cx="480" cy="927" r="9"/>
      <ellipse cx="480" cy="927" rx="4" ry="9"/>
      <line x1="471" y1="927" x2="489" y2="927"/>
      <line x1="473" y1="922" x2="487" y2="922"/>
      <line x1="473" y1="932" x2="487" y2="932"/>
    </g>
    <text class="web" x="500" y="933">www.hollisfieldfurniture.com</text>

    <polygon class="motto-band" points="419,946 780,946 764,978 435,978" fill="var(--ruby)"/>
    <text class="motto" x="598" y="967" text-anchor="middle">FIND <tspan class="strong">QUALITY</tspan> | FIND <tspan class="strong">STYLE</tspan> | FIND <tspan class="strong">COMFORT</tspan></text>

    <text class="social" x="478" y="1010">Pin us on</text>
    <circle cx="573" cy="1004" r="13" fill="var(--ruby)"/>
    <text class="social" x="604" y="1010">Like us on</text>
    <circle cx="704" cy="1004" r="13" fill="var(--ruby)"/>
  </g>
  <text class="side-label" x="592" y="1173" text-anchor="middle">BACK</text>
</svg>
</body>
</html>
```